Flowy subpage design wanted for a modern tax/accounting firm in Switzerland

--- Introduction ---
We are a tax and accounting firm in Switzerland. We provide services for expats living in Switzerland, our service is quite exclusive and modern (digital).

We just relaunched our website www.fiscorana.ch and are happy with the design, so the desired subpage (more details below) should of course fit in.

--- Main brief ---
Please see Word File attached. The page has to include the whole text (11 chapters). A very intuitive, flowy design on only one subpage (not one page per chapter) is a MUST. Also, it is key that the design is supporting the content of the individual chapters, so it would be advantageous if you'd have a good unterstanding of the text attached.

--- Further information ---
A similar example would be this one: https://www2.brennick.com/ch/en/pages/tax/articles/living-working-switzerland.html

This one is similar in what concerns the content, but NOT what we are looking for designwise. It is very simple and looks "thrown together", just not aesthetically pleasing in our opinion.

--- Final thoughts ---
- If you blow our minds with your design, we will certainly have future work for you.
- Our clients are between 20-50 years old, well educated, high income / high wealth, English speaking and living in Switzerland.
- CI/CD information:
Fonts
Montserrat regular / medium italic / bold
Colors
White #ffffffff
Darkblue #0a2b46
Darkblue 25% #b5bfc8
Darkblue 50% #8595a4
Greenblue #0d4261

We are looking forward to your designs!
Updates

Thank you very much for the submitted designs and your efforts. Unfortunately, none of the designs meet our expectations so far. Please note the following: - Designs that do not take CI into account will not be looked at more closely. - We have received many simple designs with very simple structure and accordion elements. But more important than the simple structure is an eye-catching design! Make it flowy and beautiful - We don't want pictures of Swiss vehicles, passes or other pictures that don't actively support the text. If you can make an illustration that really fits the context, fine, otherwise better leave it without. Thank you

Target Market(s)

Expats living in Switzerland. High income earners / high net worth individuals

Industry/Entity Type

tax/accounting

Number of Pages Required

1 page

Font styles to use
Other font styles liked:
• Montserrat

Colors
0054AA
0677BA
7BADD7
CADEEF
E8F1F8

Requirements
Must have
• based on general website design
Nice to have
• intuitive, flowy, attractive representation of much text
Should not have
• basic copy/paste of the text in sections :)

```html
<!DOCTYPE html>
<html lang="en">
<head>
<meta charset="utf-8">
<title>Fiscorana Advisory – Life in Switzerland</title>
<link href="https://fonts.googleapis.com/css2?family=Montserrat:ital,wght@0,400;0,500;0,600;0,700;1,500&display=swap" rel="stylesheet">
<style>
:root{
  --white:#ffffff;
  --darkblue:#0a2b46;
  --darkblue-25:#b5bfc8;
  --darkblue-50:#8595a4;
  --greenblue:#0d4261;
  --footer-top:#0f3457;
  --footer-bottom:#1d4a72;
  --lake:#1f7f8c;
  --rock:#7d8a90;
  --forest:#2e4a2c;
  --wash:#c9d0d6;
}
*{box-sizing:border-box;margin:0;padding:0}
html,body{width:1200px;height:1200px;overflow:hidden;background:var(--white)}
body{font-family:"Montserrat",sans-serif;color:var(--darkblue);position:relative}

.page{
  position:absolute;left:474px;top:0;
  width:1280px;height:6077px;
  transform:scale(0.1975);transform-origin:0 0;
  background:var(--white);overflow:hidden;
}

/* navigation */
.site-nav{position:absolute;left:0;top:0;width:1280px;height:75px;display:flex;align-items:center;padding:0 170px}
.brand{display:flex;align-items:center;gap:12px;font-weight:600;font-size:17px;letter-spacing:1px;color:var(--darkblue);line-height:1.05}
.brand-dot{width:40px;height:40px;border-radius:50%;border:3px solid var(--darkblue)}
.nav-links{margin-left:auto;display:flex;gap:22px;font-size:13px;color:var(--darkblue)}
.nav-links .current{font-weight:700;border-bottom:2px solid var(--darkblue)}

/* hero */
.hero{position:absolute;left:0;top:75px;width:1280px;height:532px;overflow:hidden}
.hero-photo{position:absolute;inset:0;background:
  linear-gradient(180deg,#6f7c83 0%,#57656b 30%,#2c5a5d 55%,#1f7f8c 70%,#24463a 88%,#1b2e26 100%)}
.hero-shape{position:absolute;inset:0}
.hero-title{position:absolute;left:170px;top:150px;color:var(--white);font-size:60px;line-height:72px;letter-spacing:1px}
.hero-title .line-one{font-weight:500}
.hero-title .line-two{font-weight:700;display:block}
.hero-title .highlight{background:var(--white);color:var(--darkblue);padding:0 10px;font-weight:600}

.eyebrow{position:absolute;left:0;width:1280px;top:620px;text-align:center;font-size:14px;letter-spacing:1px;color:var(--darkblue-50);font-weight:500}

/* chapter flow */
.flow-lines{position:absolute;left:0;top:0;width:1280px;height:6077px}
.chapter{position:absolute;left:0;width:1280px;height:277px}
.chapter-wash{position:absolute;top:-80px;width:260px;height:440px}
.chapter--right .chapter-wash{right:0;background:radial-gradient(ellipse at 100% 45%,var(--wash) 0%,rgba(201,208,214,.5) 40%,rgba(255,255,255,0) 72%)}
.chapter--left .chapter-wash{left:0;background:radial-gradient(ellipse at 0% 45%,var(--wash) 0%,rgba(201,208,214,.5) 40%,rgba(255,255,255,0) 72%)}
.chapter-photo{position:absolute;top:0;width:346px;height:277px;
  background:linear-gradient(160deg,var(--rock) 0%,#5d6a6e 30%,var(--forest) 52%,var(--lake) 70%,#3f5a2a 100%);
  box-shadow:0 18px 40px rgba(10,43,70,.25)}
.chapter--right .chapter-photo{left:764px}
.chapter--left .chapter-photo{left:170px}
.chapter-number{position:absolute;top:16px;font-size:112px;font-weight:700;line-height:1;color:var(--white);
  -webkit-text-stroke:4px var(--greenblue);paint-order:stroke fill;text-shadow:4px 6px 10px rgba(10,43,70,.35)}
.chapter--right .chapter-number{left:723px}
.chapter--left .chapter-number{left:437px}
.chapter-text{position:absolute;top:2px;width:434px}
.chapter--right .chapter-text{left:170px}
.chapter--left .chapter-text{left:676px}
.chapter-title{font-size:44px;font-weight:700;line-height:54px;color:var(--darkblue)}
.chapter-title--single{white-space:nowrap}
.chapter-subtitle{font-size:22px;line-height:26px;font-weight:400;font-style:normal;color:var(--greenblue);margin-top:4px}
.chapter-body{font-size:14px;line-height:27px;font-weight:400;color:var(--darkblue-50);text-align:justify;margin-top:18px}
.explore{display:inline-flex;align-items:center;gap:8px;margin-top:26px;font-size:13px;color:var(--greenblue);font-weight:500}

/* footer */
.site-footer{position:absolute;left:0;top:5655px;width:1280px;height:422px;
  background:linear-gradient(180deg,var(--footer-top),var(--footer-bottom));color:var(--white)}
.footer-brand{position:absolute;left:145px;top:85px;display:flex;align-items:center;gap:14px;font-size:30px;font-weight:600;letter-spacing:1px;line-height:1.05}
.footer-brand .brand-dot{width:70px;height:70px;border-color:var(--white)}
.contact{position:absolute;left:145px;top:205px;list-style:none;font-size:12px;line-height:30px}
.contact li{display:flex;align-items:center;gap:12px}
.footer-col{position:absolute;top:100px}
.footer-col h3{font-size:15px;font-weight:700;letter-spacing:.5px}
.footer-col h3::after{content:"";display:block;width:30px;height:3px;background:var(--white);margin-top:12px}
.about{left:513px;width:340px}
.about p{font-size:12px;line-height:27px;margin-top:26px;color:#d7dee5}
.quick-links{left:978px}
.quick-links ul{list-style:none;font-size:12px;line-height:30px;margin-top:22px;color:#d7dee5}
.footer-bottom{position:absolute;left:0;bottom:0;width:1280px;height:62px;border-top:1px solid rgba(255,255,255,.25);
  text-align:center;font-size:12px;line-height:62px;color:#c9d3dd}
</style>
</head>
<body>
<div class="page">

  <header class="site-nav">
    <div class="brand"><span class="brand-dot"></span><span>FISCORANA<br>ADVISORY</span></div>
    <nav class="nav-links">
      <span class="current">Home</span><span>Tax returns</span><span>More services</span><span>Swiss tax guide</span><span>About us</span>
    </nav>
  </header>

  <section class="hero">
    <div class="hero-photo" role="img" aria-label="Alpine lake with pine forest, rocky cliffs and a wooden hut"></div>
    <svg class="hero-shape" viewBox="0 0 1280 532" preserveAspectRatio="none">
      <polygon points="862,428 1280,340 1280,532" fill="#0a2b46"/>
      <polygon points="0,500 862,428 1280,532 0,532" fill="#ffffff"/>
    </svg>
    <h1 class="hero-title"><span class="line-one">HOW IS <span class="highlight">LIFE</span> IN</span><span class="line-two">SWITZERLAND?</span></h1>
  </section>

  <p class="eyebrow">OUR LIFE</p>

  <svg class="flow-lines" viewBox="0 0 1280 6077" fill="none" stroke="#b5bfc8" stroke-width="2" stroke-dasharray="5 6">
    <path d="M638 660 C700 650 830 680 830 740"/>
    <path d="M830 1065 C830 1130 459 1110 459 1191"/>
    <path d="M459 1518 C459 1600 830 1560 830 1644"/>
    <path d="M830 1971 C830 2050 459 2010 459 2097"/>
    <path d="M459 2424 C459 2505 830 2465 830 2550"/>
    <path d="M830 2877 C830 2955 459 2915 459 3003"/>
    <path d="M459 3330 C459 3410 830 3370 830 3456"/>
    <path d="M830 3783 C830 3860 459 3820 459 3909"/>
    <path d="M459 4236 C459 4315 830 4275 830 4362"/>
    <path d="M830 4689 C830 4765 459 4725 459 4815"/>
    <path d="M459 5142 C459 5220 830 5180 830 5268"/>
    <path d="M830 5595 L830 5615"/>
  </svg>

  <article class="chapter chapter--right" style="top:758px">
    <div class="chapter-wash" role="img" aria-label="Faded mountain scenery"></div>
    <div class="chapter-photo" role="img" aria-label="Alpine lake and wooden hut"></div>
    <span class="chapter-number">01</span>
    <div class="chapter-text">
      <h2 class="chapter-title chapter-title--single">Life in Switzerland</h2>
      <p class="chapter-body">To give you a small impression of what to expect when living in Switzerland, we have put together some topics for you to make your new start in Switzerland as pleasant as possible.</p>
      <span class="explore">Explore More <svg width="12" height="8" viewBox="0 0 12 8"><path d="M0 4h10M7 1l3 3-3 3" fill="none" stroke="#0d4261" stroke-width="1.4"/></svg></span>
    </div>
  </article>

  <article class="chapter chapter--left" style="top:1211px">
    <div class="chapter-wash" role="img" aria-label="Faded mountain scenery"></div>
    <div class="chapter-photo" role="img" aria-label="Alpine lake and wooden hut"></div>
    <span class="chapter-number">02</span>
    <div class="chapter-text">
      <h2 class="chapter-title">Switzerland</h2>
      <p class="chapter-subtitle">A brief overview of the Alpine country</p>
      <p class="chapter-body">Every year, Switzerland attracts many new citizens who want to settle there temporarily or long-term, and not without reason, because life in Switzerland is characterized by a high quality. If you are also thinking of settling here, we would like to introduce you to the country in the following.</p>
      <span class="explore">Explore More <svg width="12" height="8" viewBox="0 0 12 8"><path d="M0 4h10M7 1l3 3-3 3" fill="none" stroke="#0d4261" stroke-width="1.4"/></svg></span>
    </div>
  </article>

  <article class="chapter chapter--right" style="top:1664px">
    <div class="chapter-wash" role="img" aria-label="Faded mountain scenery"></div>
    <div class="chapter-photo" role="img" aria-label="Alpine lake and wooden hut"></div>
    <span class="chapter-number">03</span>
    <div class="chapter-text">
      <h2 class="chapter-title">Immigrating to<br>Switzerland</h2>
      <p class="chapter-subtitle">These options are available</p>
      <p class="chapter-body">Depending on which citizenship(s) an immigrant to Switzerland holds, immigration regulations differ. In this article we explain everything you need to know or consider about immigrating to Switzerland.</p>
      <span class="explore">Explore More <svg width="12" height="8" viewBox="0 0 12 8"><path d="M0 4h10M7 1l3 3-3 3" fill="none" stroke="#0d4261" stroke-width="1.4"/></svg></span>
    </div>
  </article>

  <article class="chapter chapter--left" style="top:2117px">
    <div class="chapter-wash" role="img" aria-label="Faded mountain scenery"></div>
    <div class="chapter-photo" role="img" aria-label="Alpine lake and wooden hut"></div>
    <span class="chapter-number">04</span>
    <div class="chapter-text">
      <h2 class="chapter-title">Labor Law in<br>Switzerland</h2>
      <p class="chapter-subtitle">An Overview</p>
      <p class="chapter-body">Anyone who is gainfully employed in Switzerland is protected by Swiss labor law and is also subject to its rules. We explain everything you need to know about employment law in Switzerland and what rights and obligations you have as part of your employment.</p>
      <span class="explore">Explore More <svg width="12" height="8" viewBox="0 0 12 8"><path d="M0 4h10M7 1l3 3-3 3" fill="none" stroke="#0d4261" stroke-width="1.4"/></svg></span>
    </div>
  </article>

  <article class="chapter chapter--right" style="top:2570px">
    <div class="chapter-wash" role="img" aria-label="Faded mountain scenery"></div>
    <div class="chapter-photo" role="img" aria-label="Alpine lake and wooden hut"></div>
    <span class="chapter-number">05</span>
    <div class="chapter-text">
      <h2 class="chapter-title">Double Taxation</h2>
      <p class="chapter-subtitle">Agreements between Switzerland<br>and other countries</p>
      <p class="chapter-body">In order to avoid the income and assets of an individual living in Switzerland but having income or assets in another country, Switzerland has concluded double taxation agreements with many countries.</p>
      <span class="explore">Explore More <svg width="12" height="8" viewBox="0 0 12 8"><path d="M0 4h10M7 1l3 3-3 3" fill="none" stroke="#0d4261" stroke-width="1.4"/></svg></span>
    </div>
  </article>

  <article class="chapter chapter--left" style="top:3023px">
    <div class="chapter-wash" role="img" aria-label="Faded mountain scenery"></div>
    <div class="chapter-photo" role="img" aria-label="Alpine lake and wooden hut"></div>
    <span class="chapter-number">06</span>
    <div class="chapter-text">
      <h2 class="chapter-title">Indirect Taxes</h2>
      <p class="chapter-subtitle">In Switzerland</p>
      <p class="chapter-body">As in many other countries, Switzerland also has a value added tax, which every consumer has to pay. Switzerland and Liechtenstein have a common VAT area, so that import/export or the procurement and provision of services in this community of states is treated as if it were a common country.</p>
      <span class="explore">Explore More <svg width="12" height="8" viewBox="0 0 12 8"><path d="M0 4h10M7 1l3 3-3 3" fill="none" stroke="#0d4261" stroke-width="1.4"/></svg></span>
    </div>
  </article>

  <article class="chapter chapter--right" style="top:3476px">
    <div class="chapter-wash" role="img" aria-label="Faded mountain scenery"></div>
    <div class="chapter-photo" role="img" aria-label="Alpine lake and wooden hut"></div>
    <span class="chapter-number">07</span>
    <div class="chapter-text">
      <h2 class="chapter-title chapter-title--single">Other Federal Taxes</h2>
      <p class="chapter-subtitle">In Switzerland</p>
      <p class="chapter-body">In addition to VAT, there are other federal taxes in Switzerland that should not go unmentioned here, because we want to give you as broad an overview as possible of the Swiss tax system.</p>
      <span class="explore">Explore More <svg width="12" height="8" viewBox="0 0 12 8"><path d="M0 4h10M7 1l3 3-3 3" fill="none" stroke="#0d4261" stroke-width="1.4"/></svg></span>
    </div>
  </article>

  <article class="chapter chapter--left" style="top:3929px">
    <div class="chapter-wash" role="img" aria-label="Faded mountain scenery"></div>
    <div class="chapter-photo" role="img" aria-label="Alpine lake and wooden hut"></div>
    <span class="chapter-number">08</span>
    <div class="chapter-text">
      <h2 class="chapter-title">Rent And Buy</h2>
      <p class="chapter-subtitle">In Switzerland</p>
      <p class="chapter-body">The purchase and rental prices for real estate vary greatly from region to region. In highly sought-after areas or large cities, you have to dig deeper into your pocket than if you want to live in a more rural area.</p>
      <span class="explore">Explore More <svg width="12" height="8" viewBox="0 0 12 8"><path d="M0 4h10M7 1l3 3-3 3" fill="none" stroke="#0d4261" stroke-width="1.4"/></svg></span>
    </div>
  </article>

  <article class="chapter chapter--right" style="top:4382px">
    <div class="chapter-wash" role="img" aria-label="Faded mountain scenery"></div>
    <div class="chapter-photo" role="img" aria-label="Alpine lake and wooden hut"></div>
    <span class="chapter-number">09</span>
    <div class="chapter-text">
      <h2 class="chapter-title">Childcare</h2>
      <p class="chapter-subtitle">In Switzerland</p>
      <p class="chapter-body">If you are moving to Switzerland with young children who are not yet of school age, you may need a childcare option. There are numerous childcare models to choose from. Cost plays a big role in the selection, as well as the type of care.</p>
      <span class="explore">Explore More <svg width="12" height="8" viewBox="0 0 12 8"><path d="M0 4h10M7 1l3 3-3 3" fill="none" stroke="#0d4261" stroke-width="1.4"/></svg></span>
    </div>
  </article>

  <article class="chapter chapter--left" style="top:4835px">
    <div class="chapter-wash" role="img" aria-label="Faded mountain scenery"></div>
    <div class="chapter-photo" role="img" aria-label="Alpine lake and wooden hut"></div>
    <span class="chapter-number">10</span>
    <div class="chapter-text">
      <h2 class="chapter-title">Public<br>Transportation</h2>
      <p class="chapter-body">The public transport network in Switzerland is one of the best developed in the world. In urban regions, more and more people are doing without their own vehicles and are traveling by public transport instead. But in the countryside, too, public transportation is very well developed, and you can get anywhere - by train, bus, mountain railroad or boat.</p>
      <span class="explore">Explore More <svg width="12" height="8" viewBox="0 0 12 8"><path d="M0 4h10M7 1l3 3-3 3" fill="none" stroke="#0d4261" stroke-width="1.4"/></svg></span>
    </div>
  </article>

  <article class="chapter chapter--right" style="top:5288px">
    <div class="chapter-wash" role="img" aria-label="Faded mountain scenery"></div>
    <div class="chapter-photo" role="img" aria-label="Alpine lake and wooden hut"></div>
    <span class="chapter-number">11</span>
    <div class="chapter-text">
      <h2 class="chapter-title">Recreation</h2>
      <p class="chapter-body" style="margin-top:44px">What do you actually do in Switzerland when you're not working? Since free time also plays a major role in a positive work-life balance, we naturally don't want to leave this topic unmentioned here.</p>
      <span class="explore" style="margin-top:44px">Explore More <svg width="12" height="8" viewBox="0 0 12 8"><path d="M0 4h10M7 1l3 3-3 3" fill="none" stroke="#0d4261" stroke-width="1.4"/></svg></span>
    </div>
  </article>

  <footer class="site-footer">
    <div class="footer-brand"><span class="brand-dot"></span><span>FISCORANA<br>ADVISORY</span></div>
    <ul class="contact">
      <li><svg width="14" height="16" viewBox="0 0 14 16"><path d="M7 1a5 5 0 0 0-5 5c0 4 5 9 5 9s5-5 5-9a5 5 0 0 0-5-5z" fill="none" stroke="#fff" stroke-width="1.6"/><circle cx="7" cy="6" r="1.8" fill="#fff"/></svg>Office Westerberg | Lindenweg 14</li>
      <li><svg width="14" height="14" viewBox="0 0 14 14"><path d="M3 1l3 3-2 2c1 2 2 3 4 4l2-2 3 3-2 2C6 13 1 8 1 3z" fill="none" stroke="#fff" stroke-width="1.4"/></svg>Available for existing clients only</li>
      <li><svg width="14" height="12" viewBox="0 0 14 12"><rect x="1" y="1" width="12" height="10" fill="none" stroke="#fff" stroke-width="1.4"/><path d="M1 1l6 5 6-5" fill="none" stroke="#fff" stroke-width="1.4"/></svg>Available for existing clients only</li>
    </ul>
    <div class="footer-col about">
      <h3>ABOUT FISCORANA</h3>
      <p>Fiscorana Advisory was founded in 2014 with the vision to make Swiss tax matters uncomplicated and painless for expats without compromising quality or making the service unaffordable.</p>
    </div>
    <div class="footer-col quick-links">
      <h3>QUICK LINKS</h3>
      <ul><li>Tax returns</li><li>FAQ</li><li>Swiss tax guide</li><li>About us</li><li>Privacy policy</li></ul>
    </div>
    <div class="footer-bottom">2022 Fiscorana Advisory LLC All Right Reserved | Privacy Policy | Impressum</div>
  </footer>

</div>
</body>
</html>
```